Fact/Marketing Sheet(s) for Health & Wellness Plan

We are wanting to market a new program that we have for Health & Wellness Benefits for our customer Northfield Federation of Rural Fairs (NFRF). We would like to present this information in a professional format that compels the recipient/reader to act on this.
I like the format of the UofK document (see attahed)- however would adjust the photo to be something Agricultural related.
I am very interested to see other ideas that may be proposed.
In addition to the content that we are wanting to communicate at this time (see attached (NFRF Project ) I have also included our Style Guide , logos, and pattern if needed.
Members of the Northfield Federation of Rural Fairs - typically business leaders and volunteers in communities across Alberta.
- In Brand Document

```html
<!DOCTYPE html>
<html lang="en">
<head>
<meta charset="utf-8">
<title>Health and Wellness Benefits Program – Fact Sheets</title>
<link href="https://fonts.googleapis.com/css2?family=Montserrat:wght@400;600;700;800&family=Open+Sans:wght@400;600;700&display=swap" rel="stylesheet">
<style>
:root{
  --navy:#1f2a5c;
  --navy-deep:#18214b;
  --blue:#2f6db3;
  --sky:#dfe7f3;
  --ink:#2a2f3d;
  --muted:#6b7180;
  --paper:#ffffff;
  --stage:#eceef2;
  --rule:#c9d0de;
}
*{box-sizing:border-box;margin:0;padding:0}
html,body{width:1200px;height:2432px;overflow:hidden;background:var(--stage)}
body{position:relative;font-family:"Open Sans",Arial,sans-serif;color:var(--ink)}
.page{position:absolute;width:520px;height:700px;background:var(--paper);box-shadow:0 2px 10px rgba(20,30,60,.18);overflow:hidden}
.col-l{left:50px}.col-r{left:630px}
.row-1{top:40px}.row-2{top:860px}.row-3{top:1680px}

.brand{display:flex;align-items:center;gap:8px;font-family:"Montserrat",sans-serif;font-weight:800;letter-spacing:.12em;color:var(--navy);font-size:13px;text-transform:uppercase}
.brand .mark{width:14px;height:14px;background:var(--navy)}
.brand.light{color:#fff}.brand.light .mark{background:#fff}
.brand.center{flex-direction:column;gap:10px;font-size:22px}
.brand.center .mark{width:30px;height:30px}

/* cover */
.cover{background:var(--navy)}
.cover .texture{position:absolute;inset:0;background:linear-gradient(160deg,#25326b 0%,#1b2552 60%,#17204a 100%)}
.cover .brand{position:absolute;top:150px;left:0;right:0}
.cover-band{position:absolute;left:0;right:0;top:340px;height:150px;background:#fff;text-align:center;padding-top:26px}
.prepared{font-family:"Montserrat",sans-serif;font-size:10px;letter-spacing:.2em;color:var(--muted);font-weight:600}
.cover-title{font-family:"Montserrat",sans-serif;color:var(--navy);font-weight:700;font-size:21px;line-height:1.25;margin-top:8px}
.cover-year{font-size:11px;color:var(--muted);margin-top:8px}
.partner{position:absolute;left:150px;right:150px;bottom:80px;height:54px;background:#fff;display:flex;align-items:center;justify-content:center;gap:8px;font-family:"Montserrat",sans-serif;font-weight:700;font-size:10px;color:var(--navy);text-align:left;line-height:1.3;padding:0 12px}
.partner .dot{flex:none;width:20px;height:20px;border-radius:50%;background:var(--blue)}

/* inner pages */
.inner .brand{position:absolute;top:26px;left:32px}
.head-band{position:absolute;left:0;right:0;top:70px;height:96px;background:var(--navy)}
.head-title{position:absolute;left:32px;top:92px;font-family:"Montserrat",sans-serif;font-weight:700;font-size:19px;line-height:1.25;color:#fff}
.head-box{position:absolute;left:150px;right:24px;top:84px;height:68px;background:#fff;padding:14px 18px;font-family:"Montserrat",sans-serif;font-weight:700;font-size:17px;line-height:1.2;color:var(--navy)}
.body{position:absolute;left:32px;right:32px;top:190px}
h3{font-family:"Montserrat",sans-serif;font-size:12px;font-weight:800;letter-spacing:.06em;color:var(--blue);text-transform:uppercase;margin:14px 0 6px;padding-bottom:4px;border-bottom:1px solid var(--rule)}
h3:first-child{margin-top:0}
ul.list{list-style:none;font-size:9.5px;line-height:1.55}
ul.list li{padding-left:12px;position:relative}
ul.list li::before{content:"";position:absolute;left:0;top:6px;width:5px;height:5px;background:var(--blue)}
ul.sub{list-style:none;padding-left:14px;font-size:9px;color:var(--muted)}
ul.sub li::before{background:var(--rule)}
.contact-line{font-size:9px;font-weight:700;color:var(--navy);margin-top:12px}
.note{font-size:9px;line-height:1.5;color:var(--muted);margin-top:8px}
.callout{margin-top:12px;text-align:center;font-family:"Montserrat",sans-serif;font-size:10px;font-weight:700;color:var(--blue);line-height:1.4}

.highlights{display:grid;grid-template-columns:1fr 1fr;gap:10px 16px;margin-top:4px}
.hl{display:flex;gap:8px;align-items:flex-start;font-size:8.5px;line-height:1.4}
.hl svg{flex:none}
.cover-list{display:flex;gap:16px;align-items:center}
.plate{flex:none;width:130px;height:130px;border-radius:50%;background:radial-gradient(circle at 45% 40%,#f4d35e 0%,#e98a3c 40%,#6fa84f 70%,#e9ecef 71%)}

.steps{display:flex;justify-content:space-between;margin-top:18px}
.step{width:100px;text-align:center}
.step .ring{width:78px;height:78px;margin:0 auto;border-radius:50%;border:3px solid var(--navy);display:flex;flex-direction:column;align-items:center;justify-content:center;font-size:8px;line-height:1.3;padding:6px}
.step .ring b{font-family:"Montserrat",sans-serif;font-size:9px;color:var(--navy)}
.step .n{font-family:"Montserrat",sans-serif;font-weight:800;color:var(--blue);font-size:11px;margin-bottom:4px}

/* back cover */
.back .texture{position:absolute;inset:0;background:linear-gradient(150deg,#ffffff 0%,#f1f3f7 100%)}
.back .brand{position:absolute;top:150px;left:0;right:0}
.back-contact{position:absolute;top:250px;left:0;right:0;text-align:center;font-size:10px;line-height:1.6;color:var(--navy);font-weight:600}
.back-band{position:absolute;left:0;right:0;top:440px;height:110px;background:var(--navy);text-align:center;padding-top:20px;color:#fff}
.back-band .prepared{color:#b9c3dc}
.back-band .cover-title{color:#fff;font-size:18px}
.back .partner{bottom:60px;border:1px solid var(--rule)}
</style>
</head>
<body>

<!-- Cover -->
<section class="page cover col-l row-1">
  <div class="texture" role="img" aria-label="Subtle geometric brand pattern on navy"></div>
  <div class="brand light center"><span class="mark"></span>Halden Ridge Brokers</div>
  <div class="cover-band">
    <div class="prepared">PREPARED</div>
    <div class="cover-title">Health and Wellness<br>Benefits Program</div>
    <div class="cover-year">2021</div>
  </div>
  <div class="partner"><span class="dot"></span>Northfield Federation<br>of Rural Fairs</div>
</section>

<!-- Program overview -->
<section class="page inner col-r row-1">
  <div class="brand"><span class="mark"></span>Halden Ridge Brokers</div>
  <div class="head-band"></div>
  <div class="head-box">Health and Wellness<br>Benefits Program</div>
  <div class="body">
    <h3>Program Highlights</h3>
    <div class="highlights">
      <div class="hl"><svg width="26" height="26" viewBox="0 0 26 26"><circle cx="13" cy="13" r="12" fill="none" stroke="#2f6db3" stroke-width="2"/><path d="M7 13l4 4 8-8" fill="none" stroke="#2f6db3" stroke-width="2"/></svg><span>Added protection for your members and volunteers at a group rate.</span></div>
      <div class="hl"><svg width="26" height="26" viewBox="0 0 26 26"><rect x="2" y="5" width="22" height="16" rx="2" fill="none" stroke="#2f6db3" stroke-width="2"/><path d="M2 10h22" stroke="#2f6db3" stroke-width="2"/></svg><span>No start up fees and simple monthly billing for every plan.</span></div>
      <div class="hl"><svg width="26" height="26" viewBox="0 0 26 26"><path d="M13 3l9 4v6c0 5-4 9-9 10-5-1-9-5-9-10V7z" fill="none" stroke="#2f6db3" stroke-width="2"/></svg><span>Coverage options built for small rural organizations.</span></div>
      <div class="hl"><svg width="26" height="26" viewBox="0 0 26 26"><circle cx="13" cy="9" r="4" fill="none" stroke="#2f6db3" stroke-width="2"/><path d="M5 23c0-5 4-8 8-8s8 3 8 8" fill="none" stroke="#2f6db3" stroke-width="2"/></svg><span>Flexible enrolment for staff and family members.</span></div>
    </div>
    <p class="contact-line">To apply, please contact us at (555) 240-3186 or benefits@haldenridge.ca</p>
    <h3>Coverages Available</h3>
    <div class="cover-list">
      <ul class="list">
        <li>Health Spending Account / Taxable Wellness Account</li>
        <li>Life &amp; Dependent Insurance</li>
        <li>Critical Illness</li>
        <li>Employee &amp; Family Assistance Program</li>
        <li>Medical Second Opinion</li>
        <li>Accidental Death and Dismemberment</li>
        <li>Hospital Cash</li>
        <li>Final Expense</li>
      </ul>
      <div class="plate" role="img" aria-label="Photo of a plate of fresh farm produce"></div>
    </div>
  </div>
</section>

<!-- Critical illness -->
<section class="page inner col-l row-2">
  <div class="brand"><span class="mark"></span>Halden Ridge Brokers</div>
  <div class="head-band"></div>
  <div class="head-title">Critical Illness Final Expense<br>AD&amp;D Hospital Cash</div>
  <div class="body">
    <h3>Coverage Available Up To Age 75 For:</h3>
    <ul class="list">
      <li>Employees</li>
      <li>Board Members</li>
      <li>Spouses and dependent children of employees or board members</li>
    </ul>
    <h3>Coverage Highlights</h3>
    <ul class="list">
      <li>Simple and quick application process</li>
      <li>Portable coverage that the employee or board member can take with them if they leave</li>
      <li>24/7 protection whether you are working, at home, or travelling</li>
      <li>All covered critical illness conditions are paid as one lump sum benefit</li>
    </ul>
    <p class="contact-line">To apply, please contact us at (555) 240-3186 or benefits@haldenridge.ca</p>
    <div class="steps">
      <div class="step"><div class="n">01</div><div class="ring"><b>Critical Illness</b>Up to $50,000</div></div>
      <div class="step"><div class="n">02</div><div class="ring"><b>Final Expense</b>Up to $25,000</div></div>
      <div class="step"><div class="n">03</div><div class="ring"><b>Accidental Death</b>Up to $250,000</div></div>
      <div class="step"><div class="n">04</div><div class="ring"><b>Hospital Cash</b>Up to $200 / day</div></div>
    </div>
  </div>
</section>

<!-- Spending accounts -->
<section class="page inner col-r row-2">
  <div class="brand"><span class="mark"></span>Halden Ridge Brokers</div>
  <div class="head-band"></div>
  <div class="head-box">Health Care &amp; Wellness<br>Spending Accounts</div>
  <div class="body">
    <h3>No Start Up Fees</h3>
    <ul class="list">
      <li>A health care spending account offers comprehensive health and dental benefits while giving your employees the flexibility to choose how they spend their health care dollars.</li>
      <li>Flexible wellness accounts provide employees with the means to proactively manage their physical, mental and financial well being, from memberships to lessons and equipment.</li>
      <li>These accounts can be provided to your employees in addition to your health spending account.</li>
      <li>Claims are simple and can be submitted online at any time from any device.</li>
      <li>Unused balances carry forward to the next plan year, and the employer only pays for claims actually made.</li>
    </ul>
    <p class="callout">COVERAGE IS AVAILABLE TO THE EMPLOYEES ONLY<br>AND THEIR FAMILIES</p>
    <p class="contact-line" style="text-align:center">To apply, please contact us at (555) 240-3186 or benefits@haldenridge.ca</p>
  </div>
</section>

<!-- EFAP -->
<section class="page inner col-l row-3">
  <div class="brand"><span class="mark"></span>Halden Ridge Brokers</div>
  <div class="head-band"></div>
  <div class="head-title">Employee Family Assistance<br>Program &amp; Medical<br>Second Opinion</div>
  <div class="body" style="top:200px">
    <h3>Coverage Available For:</h3>
    <ul class="list">
      <li>Employees</li>
      <li>Board Members</li>
      <li>Spouses and dependent children of employees or board members</li>
    </ul>
    <h3>Coverage Highlights</h3>
    <ul class="list">
      <li>Confidential and professional support for personal challenges and concerns to help with work and life issues before they become more serious</li>
      <li>Services include, but are not limited to:
        <ul class="list sub">
          <li>Short Term Counselling</li>
          <li>Legal Advice</li>
          <li>Financial Planning</li>
          <li>Nutritional Counselling</li>
          <li>Life Coaching</li>
        </ul>
      </li>
      <li>Medical Second Opinion provides an independent review of diagnosis and treatment from leading specialists, with answers delivered by phone or online.</li>
    </ul>
    <p class="contact-line">To apply, please contact us at (555) 240-3186 or benefits@haldenridge.ca</p>
  </div>
</section>

<!-- Back cover -->
<section class="page back col-r row-3">
  <div class="texture" role="img" aria-label="Faint geometric brand pattern on white"></div>
  <div class="brand center"><span class="mark"></span>Halden Ridge Brokers</div>
  <div class="back-contact">
    <svg width="10" height="10" viewBox="0 0 10 10" style="vertical-align:-1px"><path d="M2 1l2 2-1 1.5c.7 1.3 1.6 2.2 2.8 2.8L7 6l2 2-1.5 1.5C4 9 1 6 .5 2.5z" fill="#1f2a5c"/></svg> (555) 240-3186<br>
    <svg width="10" height="10" viewBox="0 0 10 10" style="vertical-align:-1px"><rect x=".5" y="2" width="9" height="6.5" fill="none" stroke="#1f2a5c"/><path d="M.5 2l4.5 3.5L9.5 2" fill="none" stroke="#1f2a5c"/></svg> benefits@haldenridge.ca
  </div>
  <div class="back-band">
    <div class="prepared">PREPARED</div>
    <div class="cover-title">Health and Wellness<br>Benefits Program</div>
  </div>
  <div class="partner"><span class="dot"></span>Northfield Federation<br>of Rural Fairs</div>
</section>

</body>
</html>
```